Need designers to make a boring check list funky and fun

We are an executive rental company based in Sydney. We deal in fully furnished properties for both short and long term bookings. We have a check list for home owners to help them prepare their home for guests.
We are looking for an interesting design which makes the mundane tasks seem both fun and enjoyable.
Target Market(s)
single, couples and families where they are dual income households. Highly educated, high powered jobs with little to no time and are stressed needing a break, but also needing to pay the mortgage.
Industry/Entity Type
It Company
Colors
Designer to choose colors to be used in the design.
Requirements
Must have
- images of house rooms, clean.
- our logo on it
Nice to have
- icons for each section ie person swimming for a pool
Should not have
- just text no images

```html
<!DOCTYPE html>
<html lang="en">
<head>
<meta charset="utf-8">
<title>Check List for Holiday Owners – Harbourline Stays</title>
<link href="https://fonts.googleapis.com/css2?family=Montserrat:wght@300;400;600;700;800&family=Lato:wght@400;700&display=swap" rel="stylesheet">
<style>
  :root {
    --pink: #e8194f;
    --grey: #5e5e60;
    --grey-dark: #4d4d4f;
    --text: #575757;
    --paper: #ffffff;
    --backdrop: #6a6a6a;
  }
  * { box-sizing: border-box; margin: 0; padding: 0; }
  html, body { width: 1200px; height: 1200px; overflow: hidden; }
  body {
    background: var(--backdrop);
    font-family: "Lato", sans-serif;
    color: var(--text);
    position: relative;
  }
  .spread {
    position: absolute;
    left: 60px; top: 218px;
    width: 1080px; height: 764px;
    display: flex;
    box-shadow: 0 18px 40px rgba(0,0,0,.35);
  }
  .page {
    position: relative;
    width: 540px; height: 764px;
    background: var(--paper);
    overflow: hidden;
  }
  .page__art { position: absolute; inset: 0; width: 100%; height: 100%; }

  /* ---------- back page ---------- */
  .rule { position: absolute; height: 1.5px; background: var(--pink); }
  .section-title {
    position: absolute;
    font-family: "Montserrat", sans-serif;
    font-weight: 700; font-size: 15px; color: var(--pink);
  }
  .checklist {
    position: absolute;
    list-style: none;
    font-size: 11.5px; line-height: 1.45;
  }
  .checklist li { position: relative; padding-left: 11px; }
  .checklist li::before {
    content: ""; position: absolute; left: 0; top: 7px;
    width: 4px; height: 4px; border-radius: 50%; background: var(--pink);
  }
  .ribbon {
    position: absolute;
    display: flex; align-items: center; gap: 6px;
  }
  .ribbon__icon {
    width: 30px; height: 30px; border-radius: 50%;
    border: 2px solid var(--pink); background: #fff;
    display: flex; align-items: center; justify-content: center;
    position: relative; z-index: 1;
  }
  .ribbon__label {
    background: var(--pink); color: #fff;
    font-family: "Montserrat", sans-serif; font-weight: 700; font-size: 12.5px;
    padding: 4px 22px 4px 16px; margin-left: -16px;
    clip-path: polygon(0 0, 100% 0, 90% 100%, 0 100%);
  }
  .divider-v { position: absolute; width: 1px; background: #c9c9c9; }
  .about {
    position: absolute; left: 40px; top: 494px; width: 470px;
    font-size: 11px; line-height: 1.45;
  }
  .brand {
    position: absolute;
    font-family: "Montserrat", sans-serif; font-weight: 600;
    letter-spacing: 3px; text-transform: uppercase;
    display: flex; align-items: center; gap: 8px;
  }
  .brand__mark { width: 12px; height: 12px; }
  .brand--back { left: 40px; top: 690px; color: #fff; font-size: 11px; }
  .brand--back .brand__mark { background: #fff; }
  .contact {
    position: absolute; left: 280px; top: 614px;
    list-style: none; color: #fff; font-size: 11px;
  }
  .contact li { display: flex; align-items: center; gap: 10px; margin-bottom: 6px; line-height: 1.3; }
  .contact svg { width: 15px; height: 15px; flex: none; }

  /* ---------- cover ---------- */
  .brand--cover { left: 150px; top: 62px; color: var(--pink); font-size: 14px; }
  .brand--cover .brand__mark { background: var(--pink); width: 16px; height: 16px; }
  .cover-rule { position: absolute; left: 174px; top: 88px; width: 230px; height: 1.5px; background: var(--pink); }
  .cover-photo {
    position: absolute; left: 0; top: 130px; width: 540px; height: 400px;
    background: linear-gradient(180deg, #f4f4f2 0%, #ecebe8 45%, #e3d9cb 62%, #f7f7f5 75%, #b8b4ae 100%);
  }
  .cover-title {
    position: absolute; left: 60px; top: 556px; width: 420px;
    text-align: center; color: #fff;
    font-family: "Montserrat", sans-serif; line-height: 1.1;
  }
  .cover-title__lead { display: block; font-weight: 800; font-size: 34px; }
  .cover-title__main { display: block; font-weight: 300; font-size: 34px; }
  .cover-url {
    position: absolute; left: 190px; top: 706px;
    color: #fff; font-size: 11px; letter-spacing: 4px;
  }
</style>
</head>
<body>
<main class="spread">

  <!-- back page -->
  <section class="page page--back">
    <svg class="page__art" viewBox="0 0 540 764" aria-hidden="true">
      <path d="M0,672 L250,672 L250,628 Q250,600 282,600 L540,600 L540,764 L0,764 Z" fill="var(--grey)"/>
      <path d="M0,672 L250,672 L250,764 L0,764 Z" fill="var(--grey-dark)" opacity=".35"/>
      <path d="M70,764 C150,742 320,748 540,724 L540,750 C360,766 220,762 150,764 Z" fill="var(--pink)"/>
    </svg>

    <div class="rule" style="left:280px;top:58px;width:230px"></div>
    <h2 class="section-title" style="left:40px;top:78px">POOL :</h2>
    <div class="rule" style="left:110px;top:90px;width:400px"></div>
    <ul class="checklist" style="left:40px;top:102px;width:470px">
      <li>Check pool is compliant with the council and obtain certificate</li>
      <li>Organise regular pool cleaner</li>
      <li>Leave detailed pool instructions (in guest handbook template provided)</li>
    </ul>

    <div class="ribbon" style="left:40px;top:178px">
      <span class="ribbon__icon"><svg width="16" height="16" viewBox="0 0 16 16"><rect x="5" y="4" width="6" height="11" rx="2" fill="var(--text)"/><path d="M6,4 L6,2 L12,1" stroke="var(--text)" stroke-width="1.5" fill="none"/></svg></span>
      <span class="ribbon__label">SAFETY</span>
    </div>
    <ul class="checklist" style="left:40px;top:218px;width:220px">
      <li>Provide fire extinguisher, fire blanket and first aid kit</li>
      <li>Repair leaking taps, broken tiles, etc</li>
      <li>Patch and holes in walls</li>
      <li>Check smoke alarms functioning</li>
    </ul>

    <div class="divider-v" style="left:272px;top:178px;height:130px"></div>

    <div class="ribbon" style="left:290px;top:178px">
      <span class="ribbon__icon"><svg width="16" height="16" viewBox="0 0 16 16"><path d="M3,8 L8,3 L13,8 L13,13 L3,13 Z" fill="none" stroke="var(--text)" stroke-width="1.6"/></svg></span>
      <span class="ribbon__label">INSURANCE</span>
    </div>
    <ul class="checklist" style="left:290px;top:218px;width:220px">
      <li>Get landlord and Tenants insurance</li>
      <li>Take photos of contents and of your home</li>
      <li>Lock away any valuables</li>
    </ul>

    <ul class="checklist" style="left:40px;top:334px;width:470px">
      <li>Your Almost there.... Final bits</li>
      <li>Provide 4 sets of keys for Harbourline Stays</li>
      <li>Arrange rubbish to be placed out on street when required (Harbourline Stays can arrange this at a fee)</li>
      <li>Let Harbourline Stays know of any areas which could be affected by heavy rain</li>
      <li>Cleaners come in to set up the property prior to guests arrival</li>
    </ul>

    <div class="rule" style="left:150px;top:456px;width:360px"></div>
    <h2 class="section-title" style="left:40px;top:470px">About Us :</h2>
    <p class="about">Harbourline Stays have a team of highly trained dedicated staff to help you find that 'home away from home'. Specialising in the areas of the Eastern Suburbs, CBD and Lower North Shore for some 20 years now. Offering fully furnished accommodation to suit all budgets from Budget to Luxury, Studio to 6 Bedroom Villas, a couple of nights to an extended stay we have something for everyone.</p>

    <div class="brand brand--back"><span class="brand__mark"></span>Harbourline Stays</div>

    <ul class="contact">
      <li><svg viewBox="0 0 16 16"><path d="M1,8 L8,2 L15,8 M3,7 L3,14 L13,14 L13,7" fill="none" stroke="#fff" stroke-width="1.6"/></svg><span>Lorem Ipsum is simply<br>dummy text of the printing</span></li>
      <li><svg viewBox="0 0 16 16"><path d="M4,2 L7,5 L5,7 Q7,10 9,11 L11,9 L14,12 L12,14 Q5,13 2,4 Z" fill="none" stroke="#fff" stroke-width="1.3"/></svg><span>+61 400 000 123</span></li>
      <li><svg viewBox="0 0 16 16"><rect x="1.5" y="3.5" width="13" height="9" fill="none" stroke="#fff" stroke-width="1.3"/><path d="M1.5,3.5 L8,9 L14.5,3.5" fill="none" stroke="#fff" stroke-width="1.3"/></svg><span>hello@harbourline.example</span></li>
      <li><svg viewBox="0 0 16 16"><circle cx="8" cy="8" r="6.5" fill="none" stroke="#fff" stroke-width="1.3"/><ellipse cx="8" cy="8" rx="3" ry="6.5" fill="none" stroke="#fff" stroke-width="1.1"/><path d="M1.5,8 L14.5,8" stroke="#fff" stroke-width="1.1"/></svg><span>www.harbourline.example</span></li>
    </ul>
  </section>

  <!-- front cover -->
  <section class="page page--cover">
    <div class="brand brand--cover"><span class="brand__mark"></span>Harbourline Stays</div>
    <div class="cover-rule"></div>

    <div class="cover-photo" role="img" aria-label="Photo of a bright, clean living room with a white sectional sofa, patterned cushions, glass coffee table and two framed prints on the wall"></div>

    <svg class="page__art" viewBox="0 0 540 764" aria-hidden="true">
      <path d="M0,764 L0,560 Q0,500 62,500 L540,500 L540,764 Z" fill="var(--grey)"/>
      <path d="M0,722 C140,700 360,696 540,662 L540,764 L0,764 Z" fill="var(--pink)"/>
    </svg>

    <h1 class="cover-title">
      <span class="cover-title__lead">CHECK LIST FOR</span>
      <span class="cover-title__main">HOLIDAY OWNERS</span>
    </h1>
    <p class="cover-url">www.harbourline.example</p>
  </section>

</main>
</body>
</html>
```